Ledgerwise Reach - B2B Demand Generation Website Project

We need a fully functional website for www.ledgerwisereach.example. We are a B2B Demand Generation company, based in London, working with companies such as QRT, VKD, Norvex, Brindlow, Tarvo generating them sales leads for their sales teams. We run this through digital marketing newsletter promotions and have a network of websites. Content syndication, data, demand generation, online marketing. Our logo has just been redone (attached) and we have a holding page already which i would like to use the style / colours. Our logo is bright and vibrant but i dont want the site to be a rainbow. We are expensive, classy, professorial, B2B, intelligent.

Home
About Us
Our Services
Prospora & QA Technology
Intent Data
Testimonials
Contact Us
Updates

Target Market(s)

B2B Marketers (QRT, Velquarion, Tarvo, VKD, Opal Reach, Driftmoor, Harlow Quantis, Technology Companies, Data Companies, Marketing Teams, Tumbleden.

Industry/Entity Type

Marketing

Coding

Coded - Design and coding required

Number of Pages Required

5+ page

Font styles to use
Sans Serif

Requirements
Must have
• Home
About Us
Our Services
Prospora & QA Technology
Intent Data
Testimonials
Contact Us

Simple Pages.

Look classy, intelligent, data experts. I like the video homepages were the image moves at the top. Very soft animation.
Nice to have
• Websites i like:

https://www.vkd.example/
https://www.brevantor.example/
https://www.plumfieldsites.example.co.uk/

Ledgerwise Reach - The Demand Generation Company
Should not have
• Glimpsevault crap images

```html
<!DOCTYPE html>
<html lang="en">
<head>
<meta charset="utf-8">
<title>Ledgerwise Reach - The Demand Generation Company</title>
<link href="https://fonts.googleapis.com/css2?family=Open+Sans:wght@400;600;700&display=swap" rel="stylesheet">
<style>
:root{
  --navy:#06142b;
  --deep:#0b2a52;
  --blue:#1c5b99;
  --bright:#2f86d0;
  --ink:#3a3a3a;
  --text:#333;
  --footer:#2a2a2a;
  --white:#fff;
}
*{box-sizing:border-box;margin:0;padding:0}
html,body{width:1200px;height:5252px;overflow:hidden}
body{position:relative;font-family:"Open Sans",Arial,sans-serif;color:var(--text);background:var(--white)}
.block{position:absolute;left:0;width:1200px}

/* header */
.site-header{top:0;height:112px;background:var(--white);display:flex;align-items:center;justify-content:space-between;padding:0 26px 0 48px}
.brand{display:flex;align-items:center;gap:12px}
.brand-square{width:22px;height:22px;background:var(--blue)}
.brand-name{color:var(--ink);font-size:24px;font-weight:600;line-height:1}
.main-nav{display:flex;height:112px;align-items:center;font-size:12.5px}
.main-nav a{color:#333;text-decoration:none;padding:0 14px;height:112px;display:flex;align-items:center}
.main-nav a.active{background:var(--blue);color:var(--white);font-weight:600;padding:0 18px}

/* hero */
.hero{top:112px;height:693px;background:radial-gradient(ellipse at 30% 45%,#1b6fb8 0%,#0d3a70 35%,#061a36 70%,#030b18 100%)}
.hero-media{position:absolute;inset:0}
.hero-copy{position:absolute;top:140px;left:205px;width:790px;color:var(--white);font-size:29px;line-height:44px;text-align:center;font-weight:400}
.scroll-cue{position:absolute;top:603px;left:582px;width:36px;height:36px;border-radius:50%;border:2px solid rgba(255,255,255,.8)}
.hero-edge{position:absolute;bottom:0;left:0}

/* client strip */
.clients{top:850px;height:80px;display:flex;justify-content:space-around;align-items:center;padding:0 56px;color:#7c7c7c;font-size:22px;font-weight:600}

/* stats */
.stats{top:957px;height:241px;background:linear-gradient(100deg,#1a5c9c,#0b2c55 60%,#040d1c);clip-path:polygon(0 0,50% 66px,100% 0,100% 100%,0 100%);color:var(--white)}
.stat{position:absolute;width:260px;text-align:center}
.stat-pre{font-size:17px}
.stat-num{font-size:31px;font-weight:400;line-height:44px}
.stat-rule{width:64px;height:2px;background:var(--white);margin:10px auto 14px}
.stat-label{font-size:12px;font-weight:600}

/* headings */
.section-title{font-size:66px;font-weight:600;color:var(--ink);text-align:center;line-height:80px}

/* about */
.about{top:1288px}
.about-body{width:790px;margin:22px auto 0;font-size:13px;line-height:16px;text-align:center;color:var(--text)}
.about-body p{margin-bottom:16px}
.about-body h4{font-size:13px;font-weight:700;margin-bottom:16px}
.about-body li{list-style:none;margin-bottom:16px;font-size:12.5px}

/* services */
.services-title{top:1834px;z-index:2}
.band{background:linear-gradient(110deg,#000 0%,#071a35 30%,#164e8b 75%,#2a7ec6 100%);color:var(--white)}
.band-mql{top:1884px;height:642px;clip-path:polygon(0 0,50% 40px,100% 0,100% 581px,50% 100%,0 581px)}
.band-sql{top:3045px;height:642px;background:linear-gradient(110deg,#1b5c9d 0%,#0d3463 55%,#000 100%);clip-path:polygon(0 0,50% 70px,100% 0,100% 581px,50% 100%,0 581px)}
.service-title{font-size:23px;font-weight:400;text-align:center}
.service-body{margin:0 auto;text-align:center;font-size:15px;line-height:24px}
.service-body p+p{margin-top:24px}
.icon{display:block;margin:0 auto}
.abm{top:2565px}

/* QA */
.qa{top:3753px}
.qa-body{width:750px;margin:30px auto 0;font-size:15px;line-height:24px;text-align:center}
.qa-body p{margin-bottom:24px}
.more-btn{display:block;width:130px;height:36px;margin:-4px auto 0;border:2px solid #555;font-size:15px;line-height:32px;text-align:center;color:#333;text-decoration:none}
.product-mark{display:flex;flex-direction:column;align-items:center;margin-top:34px;gap:6px}
.product-square{width:24px;height:24px;background:#e0a030}
.product-name{font-size:26px;letter-spacing:4px;color:#333;font-weight:400}
.band-qa{top:4380px;height:163px;background:linear-gradient(100deg,#1c5e9f,#0b2b56 55%,#030a16);clip-path:polygon(0 0,100% 0,100% 100px,50% 100%,0 100px)}

/* contact */
.contact{top:4625px}
.contact-form{width:556px;margin:22px auto 0}
.field{display:block;width:100%;border:1.5px solid #777;font-family:inherit;font-size:12px;color:#444;padding:10px 14px;margin-bottom:24px;background:var(--white);resize:none}
.field-name,.field-email{height:38px}
.field-msg{height:116px;margin-bottom:30px}
.send{width:100%;height:38px;border:2px solid #333;background:var(--white);font-family:inherit;font-size:15px;font-weight:600;letter-spacing:1px}

/* footer */
.site-footer{top:5154px;height:98px;background:var(--footer);color:#ddd}
.footer-brand{position:absolute;left:44px;top:34px;color:#ccc;font-size:20px;font-weight:600}
.copyright{position:absolute;left:0;width:1200px;text-align:center;top:80px;font-size:8px}
.social{position:absolute;right:26px;top:38px;display:flex;gap:12px;font-size:12px;font-weight:600}
.legal{position:absolute;right:26px;top:80px;font-size:8px}
</style>
</head>
<body>

<header class="block site-header">
  <div class="brand">
    <span class="brand-square"></span>
    <span class="brand-name">Ledgerwise Reach</span>
  </div>
  <nav class="main-nav">
    <a class="active" href="#">Home</a>
    <a href="#">About Us</a>
    <a href="#">Our Services</a>
    <a href="#">Prospora &amp; QA Technology</a>
    <a href="#">Intent Data</a>
    <a href="#">Testimonials</a>
    <a href="#">Contact Us</a>
  </nav>
</header>

<section class="block hero">
  <div class="hero-media" role="img" aria-label="Abstract blue digital data backdrop with glowing light streams"></div>
  <p class="hero-copy">Ledgerwise Reach offers multi-channel demand generation services to publishers and technology vendors through our network of lead generation websites and native speaking telemarketing agents. Whether looking for MQL, ABM or BANT campaigns, Ledgerwise Reach can assist you in delivering your demand generation strategy and generate pipeline for your sales teams and/or channel partners.</p>
  <span class="scroll-cue"></span>
  <svg class="hero-edge" width="1200" height="70" viewBox="0 0 1200 70"><polygon points="0,2 600,70 1200,2 1200,70 0,70" fill="#fff"/></svg>
</section>

<div class="block clients">
  <span>QRT</span><span>Tarvo</span><span>VKD</span><span>Kestrune</span><span>Pellary</span><span>Ostravin</span><span>Marrowline</span><span>Quillant</span><span>Vendaro</span>
</div>

<section class="block stats">
  <div class="stat" style="left:109px;top:92px"><div class="stat-pre">Ticker to</div><div class="stat-num">70,000+</div><div class="stat-rule"></div><div class="stat-label">Downloads Per Month</div></div>
  <div class="stat" style="left:470px;top:118px"><div class="stat-pre">Ticker to</div><div class="stat-num">25,000+</div><div class="stat-rule"></div><div class="stat-label">Leads Delivered Per Month</div></div>
  <div class="stat" style="left:828px;top:92px"><div class="stat-pre">Ticker to</div><div class="stat-num">50+</div><div class="stat-rule"></div><div class="stat-label">Countries We Can Reach</div></div>
</section>

<section class="block about">
  <h2 class="section-title">About Us</h2>
  <div class="about-body">
    <p>Ledgerwise Reach can deliver high quality sales leads from any country in the world. This can include leads via email or telemarketing, account-based targeting (ABM) or identifying need and pain points through BANT / SQL campaigns.</p>
    <p>Ledgerwise Reach offer expert demand generation support, from providing detailed leads of qualified decision-makers, to a comprehensive lead generation and SQL service.</p>
    <p>Our extensive and ongoing research campaigns give you the ability to build contact lists that identify individuals at all stages of the buying cycle, from pre-sales to sales ready.</p>
    <p>With access to over 31 million names, Ledgerwise Reach offers a range of marketing options that allow you to use our data to target the decision makers you need to reach.</p>
    <h4>This can include:</h4>
    <ul>
      <li>Breakdown by geography, job title, role and responsibility</li>
      <li>Targeting through previous research and buying intention</li>
      <li>Email dispatch to selected individuals</li>
      <li>Extensive telemarketing options</li>
    </ul>
  </div>
</section>

<h2 class="block section-title services-title">Our Services</h2>

<section class="block band band-mql">
  <h3 class="service-title" style="margin-top:118px">Marketing Qualified Leads (MQL)</h3>
  <div class="service-body" style="width:720px;margin-top:22px">
    <p>A Marketing Qualified Lead (MQL) is a prospect that has expressed an interest in what your brand has to offer. An MQL has taken the first steps to becoming a customer and is ready to receive additional contact from your company. From a very general perspective: Marketing Qualified Leads turn into Sales Qualified Leads (SQLs), which in turn can convert into customers once they have been through the buyer's journey.</p>
    <p>It's important for each potential customer to travel through all stages of the buying journey and the MQL is the first step in this process. This engagement warms them up to your brand, builds trust and puts them in the position to consider your solution as the right fit for their business.<br>The MQL is the foundation of a B2B demand generation strategy and helps businesses identify those prospects who could be in the market for their solutions.</p>
  </div>
  <svg class="icon" style="margin-top:40px" width="120" height="108" viewBox="0 0 120 108" fill="none" stroke="#fff" stroke-width="2.5"><rect x="4" y="4" width="112" height="72"/><line x1="4" y1="16" x2="116" y2="16"/><line x1="30" y1="32" x2="90" y2="32"/><line x1="30" y1="42" x2="90" y2="42"/><line x1="30" y1="52" x2="90" y2="52"/><line x1="30" y1="62" x2="70" y2="62"/><circle cx="60" cy="88" r="12"/><circle cx="60" cy="88" r="4"/></svg>
</section>

<section class="block abm">
  <h3 class="service-title" style="color:#333">Account Based Marketing Leads (ABM)</h3>
  <div class="service-body" style="width:930px;margin-top:20px;color:#333">
    ABM is a strategy that directs marketing resources to engaging a specific set of target accounts. Instead of casting a wide net to engage any potential customers, marketers use ABM and work closely with sales to identify key prospects and then tailor customized programs and messages to the buying team within target accounts.<br>
    This approach looks at prospects as Accounts rather than Individuals and takes the approach that in order to win business we must look at all stakeholders in the decision-making process.<br>
    This strategy is particularly important in today's world of work, as according to Corvane, 73% of B2B buyers are now millennials and millennials actively seek consensus and collaboration. This has created a culture of "We" not "I" in the way technology purchasing decisions are made.<br>
    Adopting an intelligent ABM strategy for demand generation can be a great way to target potential new customers. But it must be done right…<br>
    The accounts you are looking to target must have intelligence behind them for the campaign to be considered a true ABM campaign. We can help with in this process of identifying accounts you should be targeting through our Intent partnerships and own first party data and speak to you about other strategies that have been successful in the past.
  </div>
  <svg class="icon" style="margin-top:34px" width="124" height="116" viewBox="0 0 124 116" fill="none" stroke="#333" stroke-width="2.5"><polygon points="14,40 62,22 110,40 62,58"/><polyline points="14,40 14,90 62,112 110,90 110,40"/><line x1="62" y1="58" x2="62" y2="112"/><polyline points="14,40 2,56 50,76 62,58"/><polyline points="110,40 122,56 74,76 62,58"/><path d="M56,38 V8 M50,14 L56,8 L62,14 M70,36 V4 M64,10 L70,4 L76,10"/></svg>
</section>

<section class="block band band-sql">
  <h3 class="service-title" style="margin-top:128px">Sales Qualified Lead / BANT</h3>
  <div class="service-body" style="width:740px;margin-top:14px">
    An SQL lead or a BANT lead is a type of lead that expressed a specific interest in a product and service that you have to offer…<br>
    The difference between marketing qualified leads (MQL) and sales qualified leads (SQL) is important to understanding your sales funnel, and perhaps most importantly, the potential bottlenecks within it.<br>
    SQLs are prospects that have been vetted to determine if there's an interest to connect them to the next stage in the buying cycle, sometimes called the Discovery or Demo stage. Commonly, BANT qualification methodology has been used by sales to define what constitutes a 'quality' lead. Budget, Authority, Need, and Timing are all criteria that need to be established but are they sufficient enough to enable your sales teams to close a deal.<br>
    We are able to offer BANT / SQL leads globally whether the target is IT, Hr, Marketing &amp; Sales. Finance or Business Decision Makers.
  </div>
  <svg class="icon" style="margin-top:30px" width="120" height="118" viewBox="0 0 120 118" fill="none" stroke="#fff" stroke-width="2.5"><circle cx="42" cy="78" r="22"/><circle cx="42" cy="78" r="9"/><circle cx="84" cy="40" r="20"/><circle cx="84" cy="40" r="8"/><circle cx="40" cy="28" r="12"/><circle cx="40" cy="28" r="4"/><circle cx="42" cy="78" r="30" stroke-dasharray="6 6"/><circle cx="84" cy="40" r="27" stroke-dasharray="6 6"/></svg>
</section>

<section class="block qa">
  <h2 class="section-title">QA Technology</h2>
  <div class="qa-body">
    <p>Prospora is a proprietary lead verification platform from Ledgerwise Reach that aims to sift out invalid leads with questionable or erroneous data. The platform is designed to equip sales teams with accurate, high-quality records in order to improve lead generation, accelerate pipeline and increase revenue.</p>
    <p>Prospora is positioned to quickly identify, validate, and improve lead quality at the point-of-entry by filtering out all leads that do not match required filters, such as job title, company size, etc. The platform is designed to use real-time contact validation and live phone verification to remove all duplicate leads, as well as leads with invalid data components. Users can also build their own rules-based, post-submission verification protocol on our forms.</p>
    <p>Our goal is to provide the most accurate lead data to ensure the best opportunity for nurture and follow up by sales and marketing teams.</p>
  </div>
  <a class="more-btn" href="#">MORE TEXT</a>
  <div class="product-mark"><span class="product-square"></span><span class="product-name">PROSPORA</span></div>
</section>

<div class="block band-qa" role="img" aria-label="Abstract blue digital network backdrop"></div>

<section class="block contact">
  <h2 class="section-title">Contact Us</h2>
  <form class="contact-form">
    <input class="field field-name" type="text" placeholder="Your name...">
    <input class="field field-email" type="email" placeholder="Your email...">
    <textarea class="field field-msg" placeholder="Your message..."></textarea>
    <button class="send" type="button">SEND</button>
  </form>
</section>

<footer class="block site-footer">
  <div class="footer-brand">Ledgerwise Reach</div>
  <div class="copyright">© 2020 Ledgerwise Reach</div>
  <div class="social"><span>Chirpnet</span><span>Pixgram</span><span>Pinwell</span></div>
  <div class="legal">Terms and Conditions | Privacy Policy | Cookie Policy</div>
</footer>

</body>
</html>
```